Business Card Project

Hello,

Please find attached files for use for our business card design.

We have attached all the version of the trade licensing council to the project for insertion onto our business card.

Details to be on the card are:
We are a construction management company. Please ensure that there is space to add our personal contact details. We would like the cards to be double sided with our logo on one side and our details on the other

Thanks,

Marcus

Good Evening,

Please ensure with all design submissions, that the 'certified works overseer' logo is on the card designs.

Thanks,

Marcus

Industry/Entity Type

Construction

```html
<!DOCTYPE html>
<html lang="en">
<head>
<meta charset="utf-8">
<title>Halvard Group – Business Card</title>
<link rel="stylesheet" href="https://fonts.googleapis.com/css2?family=Arimo:wght@400;700&family=Marcellus+SC&family=Open+Sans:wght@400;700&display=swap">
<style>
  :root {
    --page-bg: #e4e3e8;
    --card-bg: #ffffff;
    --brand-brown: #4a2412;
    --brand-grey: #6f6f6f;
    --text-grey: #8a8a8a;
    --ink: #1e1e1e;
    --rule: #c9c9c9;
  }
  * { box-sizing: border-box; margin: 0; padding: 0; }
  html, body {
    width: 1200px; height: 900px; overflow: hidden;
    background: var(--page-bg);
  }
  .sheet {
    position: relative; width: 1200px; height: 900px;
  }
  .card {
    position: absolute; top: 300px;
    width: 520px; height: 300px;
    background: var(--card-bg);
    box-shadow: 0 4px 10px rgba(0,0,0,0.25);
  }
  .card--front { left: 60px; }
  .card--back  { left: 620px; }

  /* Front */
  .front-mark-area {
    position: absolute; left: 170px; top: 70px;
    width: 180px; height: 70px;
    background: linear-gradient(90deg, var(--brand-grey), var(--brand-brown));
    opacity: 0.85;
  }
  .wordmark {
    position: absolute; left: 0; right: 0; top: 150px;
    text-align: center;
    font-family: "Arimo", sans-serif; font-weight: 700;
    font-size: 56px; line-height: 1; letter-spacing: 1px;
    color: var(--brand-brown);
  }
  .wordmark-rule {
    position: absolute; top: 181px; width: 80px; height: 2px;
    background: linear-gradient(90deg, transparent, var(--rule), transparent);
  }
  .wordmark-rule--left  { left: 30px; }
  .wordmark-rule--right { right: 30px; }
  .wordmark-tag {
    position: absolute; left: 0; right: 0; top: 214px;
    text-align: center;
    font-family: "Arimo", sans-serif; font-size: 9px;
    color: var(--brand-grey);
  }

  /* Back */
  .back-mark-area {
    position: absolute; left: 0; top: 40px;
    width: 340px; height: 150px;
    background: linear-gradient(90deg, var(--brand-grey) 0%, var(--brand-brown) 45%, var(--brand-grey) 100%);
    opacity: 0.9;
  }
  .holder {
    position: absolute; right: 30px; top: 32px; text-align: right;
  }
  .holder-name {
    font-family: "Marcellus SC", serif; font-size: 20px; color: var(--ink);
    letter-spacing: 0.5px;
  }
  .holder-role {
    font-family: "Open Sans", sans-serif; font-style: italic; font-size: 12px;
    color: var(--ink); margin-right: 34px;
  }
  .contact {
    position: absolute; left: 18px; top: 204px;
    font-family: "Arimo", sans-serif; color: var(--text-grey);
  }
  .contact-phone { font-size: 16px; }
  .contact-line  { font-size: 11.5px; line-height: 1.25; }
  .contact-address { font-size: 9px; line-height: 1.3; margin-top: 8px; }

  .accreditation {
    position: absolute; right: 24px; bottom: 22px;
    display: flex; align-items: center; gap: 6px;
  }
  .accreditation-seal {
    width: 28px; height: 28px; border-radius: 50%;
    border: 2px solid var(--brand-grey); background: #f1f1f1;
  }
  .accreditation-text {
    font-family: "Open Sans", sans-serif; color: var(--ink); line-height: 1.05;
  }
  .accreditation-title { font-size: 13px; font-weight: 700; }
  .accreditation-sub   { font-size: 9.5px; font-weight: 700; }
</style>
</head>
<body>
<main class="sheet">
  <section class="card card--front" aria-label="Business card front">
    <div class="front-mark-area" role="img" aria-label="Space for the company building emblem"></div>
    <span class="wordmark-rule wordmark-rule--left"></span>
    <span class="wordmark-rule wordmark-rule--right"></span>
    <h1 class="wordmark">HALVARD</h1>
    <p class="wordmark-tag">Group</p>
  </section>

  <section class="card card--back" aria-label="Business card back">
    <div class="back-mark-area" role="img" aria-label="Large company building emblem decoration"></div>
    <div class="holder">
      <p class="holder-name">Name Surname</p>
      <p class="holder-role">profession</p>
    </div>
    <address class="contact" style="font-style:normal">
      <p class="contact-phone">(000)000-0000</p>
      <p class="contact-line">email@website.com</p>
      <p class="contact-line">www.website.com</p>
      <p class="contact-address">Street, Building, Zip Code,<br>City, Country</p>
    </address>
    <div class="accreditation">
      <span class="accreditation-seal"></span>
      <div class="accreditation-text">
        <p class="accreditation-title">CERTIFIED</p>
        <p class="accreditation-sub">Works Overseer</p>
      </div>
    </div>
  </section>
</main>
</body>
</html>
```